Web Design Project - Corvellian

I want to take the existing logo, add a strapline to it and update the logo files. I then need to design powerpoint template and MS Word template for our collateral as well as 9cm x 5cm business card design for 5 people. I then want to design the website look and feel, and get whatever advice I can on coding it and next steps. Consistent message, innovation and technical ability are what I'm pushing. We are supplying Water Companies, Oil and Gas and Contractors with machinery and products to repair pipelines without digging up the ground, otherwise known as trenchless rehabilitation. I will need some help on content as well. one of our partners is www.kolvmarden.example we need to include their products and can use their content. I will need the ability to add to the site , I think it is called CMS.
Updates

Thanks for your input so far, the strap line is Renewable Infrastructure Solutions. I want to work it into the logo to make it seem part of it as opposed to just added text.

I have uploaded the existing business card design, I like this so, I want to add to this design rather than change it, it needs to be 9cm x 5.5cm. I would like to see some vertical designs as well as horizontal.

apologies I have been away, I will provide feedback ASAP

Target Market(s)

contractors, government, engineers, urban planners, environmentalists, degree level

Industry/Entity Type

Business

Requirements
Must have
• It must be compliant with all ios devices and fully windows and mac compatible.
No flash
Nice to have
• some sort of dynamic content

```html
<!DOCTYPE html>
<html lang="en">
<head>
<meta charset="utf-8">
<title>Corvellian Letterhead</title>
<link href="https://fonts.googleapis.com/css2?family=Montserrat:wght@500&family=PT+Sans:wght@400&display=swap" rel="stylesheet">
<style>
  :root {
    --frame: #e4e4e4;
    --paper: #ffffff;
    --brand-grey: #8e8e8e;
    --brand-green: #77b852;
    --blue-light: #0092cc;
    --blue-mid: #0080b6;
    --blue-deep: #004f6d;
    --footer-text: #ffffff;
  }
  html, body {
    margin: 0;
    padding: 0;
    overflow: hidden;
  }
  body {
    width: 852px;
    height: 1200px;
    background: var(--frame);
  }
  .letterhead {
    position: absolute;
    left: 5px;
    top: 5px;
    width: 842px;
    height: 1190px;
    background: var(--paper);
    overflow: hidden;
  }
  .brand {
    position: absolute;
    left: 9px;
    top: 40px;
    display: flex;
    align-items: center;
    gap: 12px;
  }
  .brand-name {
    font-family: "Montserrat", sans-serif;
    font-weight: 500;
    font-size: 27px;
    letter-spacing: 1px;
    color: var(--brand-grey);
    line-height: 1;
    text-transform: uppercase;
  }
  .brand-mark {
    width: 18px;
    height: 18px;
    background: var(--brand-green);
  }
  .header-band {
    position: absolute;
    left: 0;
    top: 0;
  }
  .footer-bands {
    position: absolute;
    left: 0;
    top: 1126px;
  }
  .footer-address,
  .footer-contact {
    position: absolute;
    top: 1133px;
    font-family: "PT Sans", sans-serif;
    font-size: 14px;
    line-height: 22px;
    color: var(--footer-text);
    margin: 0;
  }
  .footer-address {
    left: 21px;
  }
  .footer-contact {
    right: 17px;
    text-align: right;
  }
</style>
</head>
<body>
  <main class="letterhead">
    <svg class="header-band" width="842" height="60" viewBox="0 0 842 60" aria-hidden="true">
      <polygon points="277,9 835,9 835,46 315,46" fill="var(--brand-green)"/>
    </svg>

    <div class="brand">
      <span class="brand-name">Corvellian</span>
      <span class="brand-mark" aria-hidden="true"></span>
    </div>

    <svg class="footer-bands" width="842" height="64" viewBox="0 0 842 64" aria-hidden="true">
      <defs>
        <linearGradient id="footerBlue" x1="0" y1="0" x2="1" y2="0">
          <stop offset="0" stop-color="var(--blue-light)"/>
          <stop offset="1" stop-color="var(--blue-mid)"/>
        </linearGradient>
      </defs>
      <polygon points="8,0 387,0 445,56 8,56" fill="url(#footerBlue)"/>
      <polygon points="396,0 834,0 834,56 454,56" fill="var(--blue-deep)"/>
    </svg>

    <address class="footer-address">
      55, Building name, Street name<br>
      City - Zip code
    </address>
    <p class="footer-contact">
      Call us : 555 210 4870, 555 318 2964<br>
      Email : info@corvellian.example
    </p>
  </main>
</body>
</html>
```